exclusive Speakeasy Bar Web design in New Jersey USA

We are opening a speakeasy in New Jersey USA soon. we are looking for a web designer to do our web site including the coding. we a looking for a 4 to 5 page web design. the site will be mostly static. home page, contact page, menu page and a link to a 3rd party site (most likely Qelmo) for reservations. we are looking for this designer to do our menu deign as well. we are looking for a quick turnaround 7-10 days. i am attaching some pictures for the designers to see the concept design and the actual current pictures with our logo as well. professionally taken pictures will be provided later on. our photographer will be taking the pictures in the next week.

Industry/Entity Type

Restaurant, Bar, Speakeasy

Coding

Coded - Design and coding required

Number of Pages Required

4 page

Requirements
Must have
• home page, contact page, menu page and a link to qelmo.com for reservations
Nice to have
• some videos

```html
<!DOCTYPE html>
<html lang="en">
<head>
<meta charset="utf-8">
<title>Parlor 88 — Speakeasy Bar</title>
<link href="https://fonts.googleapis.com/css2?family=Bebas+Neue&family=Mr+Dafoe&family=Roboto:wght@400;500&display=swap" rel="stylesheet">
<style>
:root{
  --bg:#000;
  --ink:#fff;
  --red:#e0262b;
  --gold:#c9a24a;
  --band:#2a2724;
  --muted:#cfcfcf;
  --line:#555;
  --teal:#123440;
}
*{box-sizing:border-box;margin:0;padding:0}
html,body{width:1200px;height:5177px;overflow:hidden;background:var(--bg);color:var(--ink)}
body{position:relative;font-family:'Roboto',sans-serif}
.abs{position:absolute}
.display{font-family:'Bebas Neue',sans-serif;text-transform:uppercase;line-height:.95;letter-spacing:1px}
.script{font-family:'Mr Dafoe',cursive;color:var(--red);font-size:56px;line-height:1}
.label{font-family:'Bebas Neue',sans-serif;letter-spacing:2px;font-size:24px}
.body-copy{font-size:13px;line-height:25px;color:var(--muted)}
.photo{position:absolute}
.cta{display:flex;align-items:center;gap:12px}
.site-header{position:absolute;left:0;top:0;width:1200px;height:86px;border-bottom:1px solid var(--line)}
.site-header .vline{position:absolute;top:0;height:86px;width:1px;background:var(--line)}
.nav{position:absolute;left:112px;top:32px;display:flex;gap:34px;font-family:'Bebas Neue',sans-serif;font-size:17px;letter-spacing:1px}
.brand{position:absolute;left:555px;top:18px;width:88px;height:114px;border:2px solid #fff;display:flex;align-items:center;justify-content:center;text-align:center;font-family:'Bebas Neue',sans-serif;font-size:24px;line-height:1;background:#000}
.social{position:absolute;left:760px;top:32px;display:flex;gap:14px;font-family:'Bebas Neue',sans-serif;font-size:15px;letter-spacing:1px}
.phone{position:absolute;left:978px;top:30px;font-family:'Bebas Neue',sans-serif;font-size:20px;letter-spacing:2px}
.cat{position:absolute;top:700px;width:150px;text-align:center}
.cat .icon{width:120px;height:170px;margin:0 auto 28px;background:linear-gradient(180deg,#3a2f16,#1a1409);border-radius:8px}
.history{position:absolute;left:0;top:4495px;width:1200px;height:355px;background:var(--band)}
.badge{position:absolute;left:523px;top:4585px;width:150px;height:150px;border-radius:50%;background:var(--teal);border:2px dashed #5a7b86;text-align:center;padding-top:38px}
.info{position:absolute;left:95px;top:4920px;width:1010px;height:150px;border:1px solid #666;display:flex}
.info .cell{display:flex;align-items:center;gap:22px;padding-left:34px;font-size:13px;line-height:22px;border-right:1px solid #666}
.footer-bar{position:absolute;left:0;top:5090px;width:1200px;height:87px;background:#0c0c0c}
</style>
</head>
<body>

<header class="site-header">
  <div class="photo" role="img" aria-label="Bartender pouring a red cocktail into a martini glass" style="left:0;top:0;width:732px;height:534px;background:linear-gradient(120deg,#3a3a3c 0%,#1b1b1d 45%,#5a1420 70%,#111 100%)"></div>
  <span class="vline" style="left:86px"></span>
  <span class="vline" style="left:958px"></span>
  <nav class="nav"><span>Home</span><span>Menu</span><span>Gallery ⌄</span><span>Reservations</span></nav>
  <div class="brand">PARLOR<br>88</div>
  <div class="social"><span>Chirp</span><span>Snapline</span><span>Rated</span>
    <svg width="16" height="16" viewBox="0 0 16 16" style="margin-left:30px"><circle cx="6.5" cy="6.5" r="5" fill="none" stroke="#fff" stroke-width="2"/><line x1="10" y1="10" x2="15" y2="15" stroke="#fff" stroke-width="2"/></svg>
  </div>
  <div class="phone">555.014.2277</div>
</header>

<section>
  <div class="abs script" style="left:598px;top:192px">Parlor 88</div>
  <h1 class="abs display" style="left:598px;top:272px;font-size:92px">What makes us<br>happy</h1>
  <div class="abs cta label" style="left:598px;top:478px;font-size:22px">
    <svg width="56" height="24" viewBox="0 0 56 24"><path d="M2 12h40M34 5l9 7-9 7" fill="none" stroke="#fff" stroke-width="2"/></svg>Make a reservation</div>
</section>

<div class="abs" style="left:0;top:655px;width:1200px;height:2px;background:linear-gradient(90deg,#fff 0 80px,#444 80px 320px,transparent 320px 1160px,#666 1160px)"></div>

<section>
  <div class="cat" style="left:142px"><div class="icon" role="img" aria-label="Gold line illustration of a coffee cup"></div><div class="label">Coffee</div></div>
  <div class="cat" style="left:399px"><div class="icon" role="img" aria-label="Gold line illustration of a croissant"></div><div class="label">Bakery</div></div>
  <div class="cat" style="left:657px"><div class="icon" role="img" aria-label="Gold line illustration of a cupcake"></div><div class="label">Breakfast</div></div>
  <div class="cat" style="left:913px"><div class="icon" role="img" aria-label="Gold line illustration of a glass with ice"></div><div class="label">Drinks</div></div>
</section>

<section>
  <div class="photo" role="img" aria-label="Lounge interior with mustard velvet chairs and a mural of birds" style="left:0;top:1060px;width:788px;height:495px;background:linear-gradient(160deg,#2b2d2c,#4b4030 55%,#8a6a2a 80%,#222)"></div>
  <div class="abs script" style="left:550px;top:1160px">Parlor 88</div>
  <h2 class="abs display" style="left:550px;top:1240px;font-size:72px">I orchestrate my<br>nights to the tune of<br>a cocktail.</h2>
</section>

<section>
  <div class="photo" role="img" aria-label="Bartender garnishing a cocktail with tweezers at the bar" style="left:250px;top:1752px;width:720px;height:488px;background:linear-gradient(135deg,#1c2226,#3a3b36 50%,#6b5a2a 75%,#161616)"></div>
  <div class="abs script" style="left:85px;top:1865px">New Event</div>
  <h2 class="abs display" style="left:85px;top:1940px;font-size:76px">Turn up the heat<br>on your next<br>event.</h2>
  <p class="abs body-copy" style="left:85px;top:2182px;width:460px">Exercitation photo booth skyline tote bag Vantor, elit small batch freegan sed. Craft beer elit seitan exercitation, photo booth et 8-bit kale chips proident chillwave deep v laborum.</p>
  <div class="abs cta label" style="left:85px;top:2290px;font-size:22px">
    <svg width="56" height="24" viewBox="0 0 56 24"><path d="M2 12h40M34 5l9 7-9 7" fill="none" stroke="#fff" stroke-width="2"/></svg>Make a reservation</div>
</section>

<section>
  <h2 class="abs display" style="left:80px;top:2525px;font-size:100px;color:var(--red)">Gallery</h2>
  <div class="photo" role="img" aria-label="Back bar shelves lined with liquor bottles" style="left:0;top:2642px;width:780px;height:438px;background:linear-gradient(180deg,#2e2a26,#5a4630 50%,#1e1e20)"></div>
  <div class="photo" role="img" aria-label="Bar counter with teal stools and patterned tile floor" style="left:815px;top:2642px;width:385px;height:438px;background:linear-gradient(180deg,#222,#4a3a2c 50%,#1e4a4a 75%,#888)"></div>
  <div class="abs" style="left:1128px;top:2846px;width:30px;height:30px;background:#fff;border-radius:4px;display:flex;align-items:center;justify-content:center">
    <svg width="10" height="14" viewBox="0 0 10 14"><path d="M2 1l6 6-6 6" fill="none" stroke="#000" stroke-width="2"/></svg></div>
  <div class="abs" style="left:528px;top:3110px;width:144px;height:3px;background:#333"><div style="width:40px;height:3px;background:#aaa"></div></div>
</section>

<section>
  <div class="photo" role="img" aria-label="Hot water poured from a gooseneck kettle into a coffee dripper" style="left:0;top:3188px;width:788px;height:602px;background:linear-gradient(120deg,#2a2320,#4a3a30 50%,#8a8a88 70%,#1a1a1a)"></div>
  <svg class="abs" style="left:30px;top:3480px" width="150" height="120" viewBox="0 0 150 120"><path d="M15 110A65 65 0 0 1 140 90" fill="none" stroke="#e0262b" stroke-width="18"/></svg>
  <div class="abs script" style="left:585px;top:3290px">What's On</div>
  <h2 class="abs display" style="left:585px;top:3355px;font-size:76px">Conscience keeps<br>more people awake<br>than coffee</h2>
  <div class="abs cta label" style="left:585px;top:3612px;font-size:22px">
    <svg width="56" height="24" viewBox="0 0 56 24"><path d="M2 12h40M34 5l9 7-9 7" fill="none" stroke="#fff" stroke-width="2"/></svg>Find our bar</div>
</section>

<section>
  <div class="abs script" style="left:120px;top:3860px">Events</div>
  <h2 class="abs display" style="left:120px;top:4040px;font-size:66px">Shake it<br>today</h2>
  <p class="abs body-copy" style="left:120px;top:4195px;width:300px">The creators of the theme are happy with the response and have vowed to create further themes exploring the same concepts</p>
  <div class="abs label" style="left:120px;top:4298px;font-size:20px">Read more</div>
  <div class="photo" role="img" aria-label="Orange spritz cocktail with citrus slices" style="left:482px;top:3955px;width:281px;height:455px;background:linear-gradient(180deg,#2a1a10,#c06a1a 55%,#2a1a12)"></div>
  <div class="photo" role="img" aria-label="Glass of beer beside a burger and fries" style="left:797px;top:3955px;width:281px;height:455px;background:linear-gradient(180deg,#3a2410,#a0641c 50%,#3a2a20)"></div>
</section>

<section class="history">
  <h2 class="abs display" style="left:78px;top:58px;font-size:36px">History</h2>
  <p class="abs body-copy" style="left:78px;top:122px;width:360px;color:#ddd">Craft beer elit seitan exercitation, photo booth et 8-bit kale chips proident chillwave deep v laborum. Aliquip veniam delectus, Veldo eiusmod tempor in do umami readymade swag.</p>
  <div class="abs" role="img" aria-label="Handwritten signature" style="left:78px;top:255px;width:220px;height:40px;background:linear-gradient(90deg,#3a3633,#2a2724)"></div>
  <div class="photo" role="img" aria-label="Lit back bar with rows of bottles" style="left:600px;top:0;width:600px;height:355px;background:linear-gradient(180deg,#2a2420,#6a4a2a 50%,#1c1c1e)"></div>
</section>
<div class="badge"><div style="font-size:13px">since</div><div class="display" style="font-size:40px;margin-top:6px">2023</div></div>

<section class="info">
  <div class="cell" style="width:355px">
    <svg width="44" height="44" viewBox="0 0 24 24"><path d="M6.6 10.8a15 15 0 0 0 6.6 6.6l2.2-2.2c.3-.3.7-.4 1-.2 1.1.4 2.3.6 3.6.6.6 0 1 .4 1 1V20c0 .6-.4 1-1 1A17 17 0 0 1 3 4c0-.6.4-1 1-1h3.5c.6 0 1 .4 1 1 0 1.3.2 2.5.6 3.6.1.3 0 .7-.2 1z" fill="none" stroke="var(--gold)" stroke-width="1.4"/></svg>
    <div>Openning Hours<br>11.30AM – 2.30PM</div></div>
  <div class="cell" style="width:402px">
    <svg width="44" height="44" viewBox="0 0 24 24"><path d="M12 22s7-7 7-12a7 7 0 0 0-14 0c0 5 7 12 7 12z" fill="none" stroke="var(--gold)" stroke-width="1.4"/><circle cx="12" cy="10" r="2.5" fill="none" stroke="var(--gold)" stroke-width="1.4"/></svg>
    <div>Location Cedar Row, Linden<br>Court, NEW JERSEY, USA</div></div>
  <div class="cell" style="border-right:0;padding-left:70px;gap:14px;font-family:'Bebas Neue',sans-serif;font-size:16px;letter-spacing:1px"><span>Chirp</span><span>Snapline</span><span>Rated</span></div>
</section>

<footer class="footer-bar">
  <svg class="abs" style="left:1160px;top:48px" width="14" height="16" viewBox="0 0 14 16"><path d="M7 15V2M2 7l5-5 5 5" fill="none" stroke="#fff" stroke-width="1.6"/></svg>
</footer>

</body>
</html>
```